Business Card Re-Design/Update

We'd like to update out business cards. I've included our current "Style guide" which has the colour scheme of the organisation in it. I've also included the branding files with logos etc in them.

I've also included a copy of one of our existing cards so that you can see how ugly/dated they look. I'd like a fresh modern corporate look.

Target Market(s)

These are for our clients, potential clients, industry contacts - like all business cards

Contact Information for Business Card

Name
Position
Company Address - Level 1, 47 Garnet Lane, Toowong Qld 4066
Direct Phone
mobile
Email
Website -www.korvalnet.com.au
Logo

Colors

Designer to choose colors to be used in the design.

Requirements
Must have
• Main Logo
• Cards will need to be editable to be able to personalize them for each new employee.
Nice to have
• The MapOUT, HandOVER, UpKEEP would be okay to have if they can be sensibly and professionally added to the look without detracting from the main imagery.
• Maybe they could go on the back of the card? will leave this to your creative discretion as to whether/where they fit.
Should not have
• Should not have decorative or script fonts

```html
<!DOCTYPE html>
<html lang="en">
<head>
<meta charset="utf-8">
<title>korvalnet business card</title>
<link rel="stylesheet" href="https://fonts.googleapis.com/css2?family=Open+Sans:wght@700&family=Ubuntu:wght@400;500&display=swap">
<style>
  :root {
    --stage: #111111;
    --paper: #ffffff;
    --slate: #414143;
    --slate-faint: #383839;
    --brand-red: #d71920;
    --ink: #1b1b1c;
    --logo-grey: #3c3c3e;
    --white: #ffffff;
  }
  * { margin: 0; padding: 0; box-sizing: border-box; }
  html, body { width: 1053px; height: 1200px; overflow: hidden; background: var(--stage); }
  .canvas { position: relative; width: 1053px; height: 1200px; }

  .card { position: absolute; left: 73px; width: 850px; height: 510px; display: flex; overflow: hidden; }
  .card--front { top: 42px; }
  .card--back { top: 642px; }

  .brand-panel { background: var(--paper); display: flex; align-items: center; justify-content: center; gap: 14px; }
  .card--front .brand-panel { width: 382px; }
  .card--back .brand-panel { width: 638px; gap: 22px; }

  .wordmark { font-family: "Ubuntu", sans-serif; font-weight: 500; color: var(--logo-grey); letter-spacing: -1px; line-height: 1; }
  .card--front .wordmark { font-size: 56px; }
  .card--back .wordmark { font-size: 92px; }
  .brand-square { background: var(--brand-red); flex: none; }
  .card--front .brand-square { width: 30px; height: 30px; }
  .card--back .brand-square { width: 48px; height: 48px; }

  .details-panel { position: relative; flex: 1; background: var(--slate); }
  .person-name { position: absolute; left: 7px; top: 36px; font-family: "Open Sans", sans-serif; font-weight: 700; font-size: 61px; color: var(--white); letter-spacing: -1px; line-height: 1; white-space: nowrap; }
  .person-role { position: absolute; left: 10px; top: 108px; font-family: "Ubuntu", sans-serif; font-size: 26px; color: var(--white); letter-spacing: -0.5px; }

  .icon-rail { position: absolute; left: 0; top: 163px; width: 37px; height: 231px; background: var(--brand-red); border-radius: 0 37px 37px 0; }
  .icon-rail svg { position: absolute; left: 4px; width: 28px; height: 28px; }

  .contact-list { position: absolute; left: 50px; top: 196px; list-style: none; font-family: "Ubuntu", sans-serif; font-size: 25px; color: var(--ink); }
  .contact-list li { height: 42px; line-height: 36px; white-space: nowrap; }
  .contact-list li:nth-child(3) { height: 41px; }

  .address { position: absolute; left: 51px; top: 409px; font-family: "Ubuntu", sans-serif; font-size: 30px; line-height: 38px; color: var(--ink); letter-spacing: -0.3px; }

  .services { flex: 1; background: var(--slate); display: flex; flex-direction: column; align-items: center; justify-content: space-around; padding: 36px 0 60px; }
  .service { display: flex; flex-direction: column; align-items: center; gap: 14px; }
  .service-square { width: 44px; height: 44px; background: var(--slate-faint); }
  .service-name { font-family: "Ubuntu", sans-serif; font-weight: 500; font-size: 36px; color: var(--slate-faint); line-height: 1; }
</style>
</head>
<body>
<main class="canvas">

  <section class="card card--front" aria-label="Card front">
    <div class="brand-panel">
      <span class="brand-square"></span>
      <span class="wordmark">korvalnet</span>
    </div>
    <div class="details-panel">
      <h1 class="person-name">Maren Holt</h1>
      <p class="person-role">Business Development Manager</p>

      <div class="icon-rail" aria-hidden="true">
        <svg style="top:34px" viewBox="0 0 28 28"><rect x="1" y="1" width="26" height="26" rx="4" fill="var(--white)"/><path d="M10 6c-2 1-3 3-2 6 1.5 4 4 7 7.5 9 2 1 4 0 5-2l-3-3-2 1.5c-2-1.5-3.5-3.5-4.5-6l2-1.5z" fill="var(--brand-red)"/></svg>
        <svg style="top:82px" viewBox="0 0 28 28"><rect x="7" y="0" width="14" height="28" rx="2" fill="var(--white)"/><rect x="9" y="4" width="10" height="18" fill="var(--brand-red)"/><circle cx="14" cy="25" r="1.3" fill="var(--brand-red)"/></svg>
        <svg style="top:131px" viewBox="0 0 28 28"><rect x="2" y="6" width="24" height="16" fill="none" stroke="var(--white)" stroke-width="1.6"/><path d="M2 6l12 9 12-9M2 22l9-8M26 22l-9-8" fill="none" stroke="var(--white)" stroke-width="1.6"/></svg>
        <svg style="top:172px" viewBox="0 0 28 28"><g fill="none" stroke="var(--white)" stroke-width="1.5"><circle cx="14" cy="14" r="12"/><ellipse cx="14" cy="14" rx="5.5" ry="12"/><path d="M2 14h24M14 2v24M4.5 8h19M4.5 20h19"/></g></svg>
      </div>

      <ul class="contact-list">
        <li>+61 (0)7 3184 2057</li>
        <li>+61 (0)412 609 384</li>
        <li>holt@korvalnet.com.au</li>
        <li>www.korvalnet.com.au</li>
      </ul>

      <p class="address">Level 1, 47 Garnet Lane,<br>Toowong Qld 4066</p>
    </div>
  </section>

  <section class="card card--back" aria-label="Card back">
    <div class="brand-panel">
      <span class="brand-square"></span>
      <span class="wordmark">korvalnet</span>
    </div>
    <div class="services">
      <div class="service"><span class="service-square"></span><span class="service-name">HandOVER</span></div>
      <div class="service"><span class="service-square"></span><span class="service-name">MapOUT</span></div>
      <div class="service"><span class="service-square"></span><span class="service-name">UpKEEP</span></div>
    </div>
  </section>

</main>
</body>
</html>
```